Carpentry framing business card and logo design

We need a logo that works well with baseball caps, tee shirts and sweat shirts. We are a carpentry framing company specializing in apartment complexes and large residential communities. We work in what is known as the tri state area southeastern Pennsylvania , New Jersey and northern Delaware . We would like to see die signs using the old English letter M and royal blue colors. Also we stress WRSB compliance and safety.

Residential

Dalquist Construction Co Inc
1187 Harwick Lane
Brenford PA 19990
Rolf Dalquist
rolf1dalquist@quillmail.net
267-555-0148

```html
<!DOCTYPE html>
<html lang="en">
<head>
<meta charset="utf-8">
<title>Dalquist Construction Co Inc – Business Card</title>
<link href="https://fonts.googleapis.com/css2?family=Open+Sans:wght@400;600&display=swap" rel="stylesheet">
<style>
  :root {
    --backdrop: #e9e6e1;
    --navy: #14214f;
    --navy-deep: #12204c;
    --royal-faint: #22389a;
    --paper: #ffffff;
    --ink: #17235a;
  }
  html, body {
    margin: 0;
    width: 1200px;
    height: 900px;
    overflow: hidden;
    background: var(--backdrop);
    font-family: "Open Sans", Arial, sans-serif;
  }
  .canvas { position: relative; width: 1200px; height: 900px; }
  .card {
    position: absolute;
    width: 630px;
    height: 360px;
    box-shadow: 0 8px 24px rgba(0,0,0,0.18);
  }
  .card-back {
    left: 210px; top: 60px;
    background: var(--navy-deep);
    display: flex; align-items: center; justify-content: center;
  }
  .back-name {
    color: var(--royal-faint);
    font-weight: 600;
    font-size: 34px;
    letter-spacing: 0.5px;
  }
  .card-front {
    left: 360px; top: 480px;
    background: var(--paper);
    color: var(--ink);
  }
  .brand {
    position: absolute;
    right: 34px; top: 34px;
    display: flex; align-items: center; gap: 12px;
  }
  .brand-mark {
    width: 22px; height: 22px; border-radius: 50%;
    background: var(--navy);
  }
  .brand-name {
    font-weight: 600;
    font-size: 21px;
    color: var(--navy);
  }
  .contact {
    position: absolute;
    left: 56px; top: 170px;
  }
  .person {
    font-size: 21px;
    font-weight: 400;
    letter-spacing: 0.6px;
    text-transform: uppercase;
    margin: 0 0 12px;
  }
  .line {
    display: flex; align-items: center; gap: 10px;
    font-size: 15px;
    margin: 0 0 12px;
  }
  .line svg { width: 16px; height: 16px; fill: var(--navy); flex: none; }
  .line svg.outline { fill: none; stroke: var(--navy); stroke-width: 2.4; stroke-linejoin: round; }
</style>
</head>
<body>
<div class="canvas">
  <section class="card card-back">
    <span class="back-name">Dalquist Construction Co Inc</span>
  </section>

  <section class="card card-front">
    <div class="brand">
      <span class="brand-mark"></span>
      <span class="brand-name">Dalquist Construction Co Inc</span>
    </div>

    <div class="contact">
      <p class="person">Rolf Dalquist</p>
      <p class="line">
        <svg viewBox="0 0 24 24"><path d="M6.6 10.8a15.1 15.1 0 0 0 6.6 6.6l2.2-2.2a1 1 0 0 1 1-.25 11.4 11.4 0 0 0 3.6.57 1 1 0 0 1 1 1V20a1 1 0 0 1-1 1A17 17 0 0 1 3 4a1 1 0 0 1 1-1h3.5a1 1 0 0 1 1 1c0 1.25.2 2.45.57 3.57a1 1 0 0 1-.25 1z"/></svg>
        <span>267-555-0148</span>
      </p>
      <p class="line">
        <svg class="outline" viewBox="0 0 24 24"><rect x="2.5" y="5.5" width="19" height="13"/><path d="M2.5 5.5l9.5 7.5 9.5-7.5"/></svg>
        <span>rolf1dalquist@quillmail.net</span>
      </p>
      <p class="line">
        <svg viewBox="0 0 24 24"><path d="M12 2a7 7 0 0 0-7 7c0 5 7 13 7 13s7-8 7-13a7 7 0 0 0-7-7zm0 9.5A2.5 2.5 0 1 1 12 6.5a2.5 2.5 0 0 1 0 5z"/></svg>
        <span>1187 Harwick Lane Brenford PA 19990</span>
      </p>
    </div>
  </section>
</div>
</body>
</html>
```